New Zealand Export company needs business cards

We need new business cards to match our new logo for a company based in New Zealand who deal specifically with the Pacific Islands. We source, consolidate and ship products out of New Zealand to the Pacific Islands. Will attach our old ones and also new logo.
Would like the Islands we deal with and the areas of work we have access to, to be included on the business cards.

Contact Information for Business Card

T +64 9 571 3048
F +64 9 571 6285
12-18 Kowhai Lane, Drury, 2113
PO Box 814, Drury, Auckland 2247, New Zealand
www.falconfreight.example.nz
E sales@falconfreight.example.nz

Font styles to use
Sans Serif

Colors
85abd2
33a6d7
ffffff

Requirements
Must have
• A company of PWM

```html
<!DOCTYPE html>
<html lang="en">
<head>
<meta charset="utf-8">
<title>Falcon Freight – Business Cards</title>
<link rel="stylesheet" href="https://fonts.googleapis.com/css2?family=Roboto:wght@400;500;700&display=swap">
<style>
  :root {
    --brand-blue: #0b5aa6;
    --deep-blue: #0d4f95;
    --sky-blue: #33a6d7;
    --soft-blue: #85abd2;
    --white: #ffffff;
    --backdrop: #6b7276;
  }
  * { margin: 0; padding: 0; box-sizing: border-box; }
  html, body { width: 1200px; height: 900px; overflow: hidden; }
  body {
    background: var(--backdrop);
    font-family: "Roboto", sans-serif;
    position: relative;
  }
  .card {
    position: absolute;
    width: 700px;
    height: 400px;
    overflow: hidden;
  }
  /* Front */
  .card-front { left: 110px; top: 45px; background: var(--brand-blue); }
  .card-front .brand {
    position: absolute; left: 0; right: 0; top: 160px;
    display: flex; justify-content: center; align-items: center; gap: 18px;
  }
  .brand-mark { width: 34px; height: 34px; background: var(--white); }
  .brand-name {
    font-weight: 700; font-size: 44px; letter-spacing: 3px;
    color: var(--white); text-transform: uppercase;
  }
  .card-front .website {
    position: absolute; left: 0; right: 0; bottom: 48px;
    text-align: center; color: var(--white); font-size: 15px; letter-spacing: .3px;
  }
  /* Back */
  .card-back { left: 390px; top: 470px; background: var(--white); }
  .card-back .waves { position: absolute; inset: 0; }
  .card-back .brand { position: absolute; left: 50px; top: 95px; display: flex; align-items: center; gap: 12px; }
  .card-back .brand-mark { width: 26px; height: 26px; background: var(--brand-blue); }
  .card-back .brand-name { font-size: 32px; color: var(--brand-blue); letter-spacing: 2px; }
  .person { position: absolute; right: 60px; top: 38px; text-align: right; }
  .person-name { font-weight: 700; font-size: 20px; color: var(--deep-blue); letter-spacing: .5px; }
  .person-role {
    font-size: 12px; color: var(--sky-blue); letter-spacing: 1px;
    padding-bottom: 6px; border-bottom: 2px solid var(--sky-blue); display: inline-block;
  }
  .contact-list {
    position: absolute; right: 40px; top: 180px; list-style: none;
    color: var(--white); font-size: 15px; text-align: right;
  }
  .contact-list li { display: flex; justify-content: flex-end; align-items: center; gap: 10px; height: 27px; }
  .contact-icon {
    width: 20px; height: 20px; background: var(--white);
    display: flex; align-items: center; justify-content: center;
  }
  .address {
    position: absolute; left: 60px; bottom: 28px;
    color: var(--white); font-size: 14px; line-height: 1.4;
  }
</style>
</head>
<body>
  <section class="card card-front">
    <div class="brand">
      <span class="brand-mark"></span>
      <span class="brand-name">Falcon Freight</span>
    </div>
    <p class="website">www.falconfreight.example.nz</p>
  </section>

  <section class="card card-back">
    <svg class="waves" viewBox="0 0 700 400" width="700" height="400" aria-hidden="true">
      <path d="M0,290 C200,285 320,250 400,190 C480,130 560,115 700,105 L700,400 L0,400 Z" fill="var(--brand-blue)"/>
      <path d="M0,283 C200,278 316,243 396,183 C476,123 556,108 700,98" fill="none" stroke="var(--sky-blue)" stroke-width="4"/>
      <path d="M0,304 C150,300 260,284 340,244 C262,294 150,314 0,318 Z" fill="var(--white)"/>
      <path d="M520,150 C580,128 630,122 695,120" fill="none" stroke="var(--sky-blue)" stroke-width="2"/>
    </svg>

    <div class="brand">
      <span class="brand-mark"></span>
      <span class="brand-name">Falcon Freight</span>
    </div>

    <div class="person">
      <p class="person-name">TESSA RANGI</p>
      <p class="person-role">SALES MANAGER</p>
    </div>

    <ul class="contact-list">
      <li>+64 9 571 3048
        <span class="contact-icon"><svg width="12" height="12" viewBox="0 0 12 12"><path d="M2,1 L4,1 L5,3.5 L3.8,4.5 C4.5,6 6,7.5 7.5,8.2 L8.5,7 L11,8 L11,10 C11,10.6 10.6,11 10,11 C5,11 1,7 1,2 C1,1.4 1.4,1 2,1 Z" fill="var(--brand-blue)"/></svg></span>
      </li>
      <li>+64 9 571 6285
        <span class="contact-icon"><svg width="12" height="12" viewBox="0 0 12 12"><rect x="1" y="5" width="10" height="6" fill="var(--brand-blue)"/><rect x="3" y="1" width="6" height="4" fill="none" stroke="var(--brand-blue)" stroke-width="1.2"/></svg></span>
      </li>
      <li>sales@falconfreight.example.nz
        <span class="contact-icon"><svg width="12" height="12" viewBox="0 0 12 12"><rect x="1" y="2.5" width="10" height="7" fill="var(--brand-blue)"/><path d="M1,2.5 L6,6.5 L11,2.5" fill="none" stroke="var(--white)" stroke-width="1"/></svg></span>
      </li>
      <li>www.falconfreight.example.nz
        <span class="contact-icon"><svg width="12" height="12" viewBox="0 0 12 12"><circle cx="6" cy="6" r="5" fill="none" stroke="var(--brand-blue)" stroke-width="1.2"/><ellipse cx="6" cy="6" rx="2" ry="5" fill="none" stroke="var(--brand-blue)" stroke-width="1"/><line x1="1" y1="6" x2="11" y2="6" stroke="var(--brand-blue)" stroke-width="1"/></svg></span>
      </li>
    </ul>

    <p class="address">12-18 Kowhai Lane, Drury, 2113<br>PO Box 814, Drury, Auckland 2247, New Zealand</p>
  </section>
</body>
</html>
```